Luxury Toilet Rental Business. Wavelet Hire.

Wavelet Hire (the logo is in the uploaded files)
We RENT and SELL Luxury Trailer toilets.
- Show location, number, pricing, pictures.
- We have two stall trailers for rent AND 3 stall trailers
- We sell them too
- We want our phone number shown
- We are a local company
- Slogan: Elevate your event with Wavelet Hire. The Luxurious Loo
- We want a pricing portion
- We want the sizes shown
- We want the different rates/ prices shown
- We do 1 day rentals
- We do 1 week rentals
- We want the service area. We serve Los Angeles County, Orange County, Riverside County, San Bernardino County, and Palm Desert.
- Our location is in Santa Ana California

Target Market(s)

Event planners, wedding planners, venue planners, concerts, events, gatherings.

Industry/Entity Type

Luxury Toilet Rentals

Number of Pages Required

1 page

Font styles to use
Serif
Sans Serif

Colors
EE7325
F08F49
F5BC92
FAE3D3
FDF4ED

Requirements
Must have
• Location, pricing, pictures, available areas. Our slogan.
Nice to have
• I like the idea of having tabs that show price, a tab that shows our contact information, pictures, event ideas, and where we service (the areas we'll go to)

```html
<!DOCTYPE html>
<html lang="en">
<head>
<meta charset="utf-8">
<title>Wavelet Hire – The Luxurious Loo</title>
<link href="https://fonts.googleapis.com/css2?family=Krona+One&family=Lexend:wght@300;400;600;700&display=swap" rel="stylesheet">
<style>
:root{
  --orange:#EE7325;
  --orange-2:#F08F49;
  --peach:#F5BC92;
  --cream:#FAE3D3;
  --ivory:#FDF4ED;
  --ink:#111111;
  --text:#333333;
  --muted:#6b6b6b;
  --grey-bg:#f1f1f1;
  --white:#ffffff;
}
*{box-sizing:border-box;margin:0;padding:0}
html,body{width:1200px;height:4748px;overflow:hidden}
body{font-family:"Lexend",sans-serif;color:var(--text);background:var(--white);position:relative}
.display{font-family:"Krona One",sans-serif;text-transform:uppercase;letter-spacing:1px}
.accent{color:var(--orange)}
.btn{display:inline-block;font-family:"Krona One",sans-serif;font-size:13px;text-transform:uppercase;padding:12px 22px;border-radius:4px}
.btn-orange{background:var(--orange);color:var(--white)}
.ph{display:block}

/* Hero */
.hero{position:absolute;left:0;top:0;width:1200px;height:640px;background:linear-gradient(120deg,var(--orange) 0%,var(--orange-2) 60%,var(--peach) 100%);overflow:hidden}
.brand{position:absolute;left:70px;top:18px;display:flex;align-items:center;gap:10px;font-family:"Krona One",sans-serif;font-size:22px;color:var(--white)}
.brand-box{width:18px;height:18px;background:var(--white)}
.collage{position:absolute;left:600px;top:0;width:600px;height:640px;display:grid;grid-template-columns:repeat(4,1fr);grid-template-rows:repeat(4,1fr);gap:6px;padding:70px 10px 10px 10px}
.collage .ph{border-radius:2px}
.t1{grid-column:1/3;grid-row:1/3;background:linear-gradient(160deg,#8d8f92,#4a4c50)}
.t2{grid-column:3/4;grid-row:1/2;background:linear-gradient(160deg,#2b2140,#5a3a6e)}
.t3{grid-column:4/5;grid-row:1/2;background:linear-gradient(160deg,#c9b9a3,#6b5a4a)}
.t4{grid-column:3/5;grid-row:2/3;background:linear-gradient(160deg,#3c2f2a,#8a6a55)}
.t5{grid-column:1/2;grid-row:3/5;background:linear-gradient(160deg,#d9d4cc,#8e8a84)}
.t6{grid-column:2/4;grid-row:3/5;background:linear-gradient(160deg,#e7e6e2,#9da3a8)}
.t7{grid-column:4/5;grid-row:3/5;background:linear-gradient(160deg,#5b4a3e,#2e2622)}
.nav{position:absolute;left:440px;top:16px;display:flex;gap:26px;font-size:14px;color:var(--white)}
.hero-title{position:absolute;left:80px;top:155px;width:520px;font-size:31px;line-height:1.32;color:var(--white)}
.hero-text{position:absolute;left:80px;top:365px;width:420px;font-size:13px;line-height:1.5;color:var(--white)}
.hero-btn{position:absolute;left:80px;top:430px;border:2px solid var(--white);color:var(--white)}

/* Section titles */
.section-title{position:absolute;left:0;width:1200px;text-align:center;font-size:36px;color:var(--ink)}
.rule{position:absolute;left:550px;width:100px;height:4px;background:var(--orange)}

/* About */
.about-text{position:absolute;left:155px;top:810px;width:890px;text-align:center;font-size:14px;line-height:1.65;color:var(--text)}
.about-text p+p{margin-top:14px}
.about-btn{position:absolute;left:518px;top:1110px}

/* Rent */
.rent{position:absolute;left:0;top:1240px;width:1200px;height:700px;background:linear-gradient(180deg,#cfd3d7 0%,#a7aaad 55%,#7c7e80 100%)}
.rent-tabs{position:absolute;left:640px;top:1336px;display:flex;gap:6px}
.tab{font-family:"Krona One",sans-serif;font-size:12px;padding:8px 22px;border-radius:4px 4px 0 0;color:var(--white)}
.tab-on{background:var(--orange)}
.tab-off{background:#3a3a3a}
.rent-card{position:absolute;left:640px;top:1365px;width:420px;height:475px;background:var(--white);border-radius:10px;padding:30px 32px;box-shadow:0 10px 30px rgba(0,0,0,.25)}
.rent-card h3{font-size:30px;color:var(--ink);border-left:4px solid var(--orange);padding-left:10px}
.rent-card .desc{margin-top:14px;font-size:13px;line-height:1.5}
.label{margin-top:16px;font-size:13px;font-weight:600;color:var(--ink)}
.sizes{display:flex;justify-content:space-between;margin-top:8px;font-size:13px;padding-right:30px}
.size-line{height:1px;background:#ccc;margin-top:8px}
.select{margin-top:10px;height:38px;border:1px solid #bbb;border-radius:4px;display:flex;align-items:center;gap:8px;padding:0 10px;font-size:13px;color:var(--muted)}
.price{margin-top:22px;font-family:"Krona One",sans-serif;font-size:22px;color:var(--orange)}
.book{margin-top:16px}

/* Service areas */
.area{position:absolute;width:290px;height:320px;background:var(--white);box-shadow:0 6px 18px rgba(0,0,0,.18);padding:10px}
.area .ph{width:100%;height:245px}
.area-name{text-align:center;font-family:"Krona One",sans-serif;font-size:13px;color:var(--ink);margin-top:22px}
.area-hl{border:4px solid var(--orange)}

/* Testimonials */
.reviews{position:absolute;left:0;top:2860px;width:1200px;height:560px;background:var(--grey-bg)}
.review{position:absolute;top:3040px;width:285px}
.stars{display:flex;gap:3px}
.review h4{font-family:"Krona One",sans-serif;font-size:15px;color:var(--ink);margin-top:8px}
.review p{margin-top:10px;font-size:13px;line-height:1.55}
.arrow{position:absolute;top:3170px}

/* Reserve */
.reserve{position:absolute;left:0;top:3420px;width:1200px;height:820px;background:linear-gradient(180deg,#b8c0c8 0%,#8e949a 50%,#6f6c68 100%)}
.reserve-card{position:absolute;left:232px;top:3488px;width:736px;height:732px;background:rgba(40,40,40,.82);border-radius:24px}
.reserve-title{position:absolute;left:232px;top:3530px;width:736px;text-align:center;font-size:34px;line-height:1.35;color:var(--white)}
.form{position:absolute;left:268px;top:3662px;width:664px}
.row{display:flex;gap:8px;margin-bottom:12px}
.field{flex:1;height:44px;background:var(--white);font-size:13px;color:var(--muted);padding:12px 10px}
.field.tall{height:130px}
.submit{position:absolute;left:518px;top:4124px}

/* Footer */
.footer-brand{position:absolute;left:0;top:4300px;width:1200px;display:flex;justify-content:center;align-items:center;gap:12px;font-family:"Krona One",sans-serif;font-size:40px;color:var(--orange)}
.footer-brand .brand-box{width:26px;height:26px;background:var(--orange)}
.footer-nav{position:absolute;left:0;top:4458px;width:1200px;display:flex;justify-content:center;gap:28px;font-size:15px;color:var(--ink)}
.footer-rule{position:absolute;left:230px;top:4500px;width:740px;height:1px;background:#cfcfcf}
.contacts{position:absolute;left:230px;top:4525px;width:740px;display:flex;justify-content:space-between;font-size:13px;color:var(--ink)}
.contact{display:flex;align-items:center;gap:10px}
.copy{position:absolute;left:0;top:4630px;width:1200px;text-align:center;font-size:13px;color:var(--muted)}
.socials{position:absolute;left:0;top:4665px;width:1200px;display:flex;justify-content:center;gap:10px}
.social{width:32px;height:32px;border:2px solid var(--orange);border-radius:50%}
</style>
</head>
<body>

<!-- Hero -->
<header class="hero">
  <div class="brand"><span class="brand-box"></span>Wavelet Hire</div>
  <div class="collage">
    <div class="ph t1" role="img" aria-label="Luxury trailer restroom parked outdoors"></div>
    <div class="ph t2" role="img" aria-label="Concert crowd with stage lights"></div>
    <div class="ph t3" role="img" aria-label="Guests gathered at an outdoor event"></div>
    <div class="ph t4" role="img" aria-label="Wedding celebration guests"></div>
    <div class="ph t5" role="img" aria-label="Clean restroom trailer interior"></div>
    <div class="ph t6" role="img" aria-label="Event tent set up at a venue"></div>
    <div class="ph t7" role="img" aria-label="Guests celebrating at a party"></div>
  </div>
  <nav class="nav">
    <span>Home</span><span>Rent</span><span>Sell</span><span>Service areas</span><span>Pricing</span><span>Gallery</span><span>Event</span><span>Contact</span>
  </nav>
  <h1 class="hero-title display">Elevate your event with Wavelet Hire. The Luxurious Loo</h1>
  <p class="hero-text">Lorem ipsum dolor sit amet, consectetur adipiscing elit, sed do eiusmod tempor incididunt ut labore et dolore magna aliqua.</p>
  <span class="btn hero-btn">Get Started</span>
</header>

<!-- About -->
<h2 class="section-title display" style="top:722px">About Wavelet <span class="accent">Hire</span></h2>
<div class="rule" style="top:778px"></div>
<div class="about-text">
  <p>Lorem ipsum dolor sit amet, consectetur adipiscing elit, sed do eiusmod tempor incididunt ut labore et dolore magna aliqua. Quis ipsum suspendisse ultrices gravida. Risus commodo viverra maecenas accumsan lacus vel facilisis. Lorem ipsum dolor sit amet, consectetur adipiscing elit, sed do eiusmod tempor incididunt ut labore et dolore magna aliqua. Ut enim ad minim veniam, quis nostrud exercitation ullamco laboris nisi ut aliquip ex ea commodo consequat. Duis aute irure dolor in reprehenderit in voluptate velit esse cillum dolore eu fugiat nulla pariatur. Excepteur sint occaecat cupidatat non proident, sunt in culpa qui officia deserunt mollit anim id est laborum.</p>
  <p>Sed ut perspiciatis unde omnis iste natus error sit voluptatem accusantium doloremque laudantium, totam rem aperiam, eaque ipsa quae ab illo inventore veritatis et quasi architecto beatae vitae dicta sunt explicabo. Nemo enim ipsam voluptatem quia voluptas sit aspernatur aut odit aut fugit, sed quia consequuntur magni dolores eos qui ratione voluptatem sequi nesciunt.</p>
</div>
<span class="btn btn-orange about-btn">Learn More</span>

<!-- Rent -->
<section class="rent" role="img" aria-label="Three-stall luxury restroom trailer parked in a lot"></section>
<div class="rent-tabs"><span class="tab tab-on">Rent</span><span class="tab tab-off">Sell</span></div>
<div class="rent-card">
  <h3 class="display">For Rent</h3>
  <p class="desc">Lorem ipsum dolor sit amet, consectetur adipiscing elit, sed do eiusmod tempor incididunt ut labore.</p>
  <p class="label">Sizes</p>
  <div class="sizes"><span>Small</span><span>Mid-Size</span><span>Large</span></div>
  <div class="size-line"></div>
  <p class="label">Choose A Location</p>
  <div class="select">
    <svg width="14" height="14" viewBox="0 0 24 24"><path d="M12 2a7 7 0 0 0-7 7c0 5 7 13 7 13s7-8 7-13a7 7 0 0 0-7-7zm0 9.5A2.5 2.5 0 1 1 12 6.5a2.5 2.5 0 0 1 0 5z" fill="#888"/></svg>
    Choose a Location
  </div>
  <p class="price">$ 125.00</p>
  <span class="btn btn-orange book">Book Now</span>
</div>

<!-- Service areas -->
<h2 class="section-title display" style="top:1995px">Where We <span class="accent">Service</span></h2>
<div class="rule" style="top:2050px"></div>

<div class="area" style="left:140px;top:2100px"><div class="ph" role="img" aria-label="Los Angeles skyline" style="background:linear-gradient(180deg,#5d9be0 0%,#8fb9e4 50%,#4d5a68 100%)"></div><p class="area-name">Los Angeles</p></div>
<div class="area area-hl" style="left:455px;top:2094px;width:296px;height:332px"><div class="ph" role="img" aria-label="Orange County coastline and harbor" style="background:linear-gradient(180deg,#7fb3e6 0%,#3c7bb8 45%,#c9b08a 100%)"></div><p class="area-name" style="color:var(--orange)">Orange County</p></div>
<div class="area" style="left:770px;top:2100px"><div class="ph" role="img" aria-label="Riverside County beach and hills" style="background:linear-gradient(180deg,#9cc8ea 0%,#6aa6cf 40%,#8a9a6a 100%)"></div><p class="area-name">Riverside County</p></div>
<div class="area" style="left:297px;top:2440px"><div class="ph" role="img" aria-label="San Bernardino mountains view" style="background:linear-gradient(180deg,#a9c2d8 0%,#b5a992 55%,#7a6f5e 100%)"></div><p class="area-name">San Bernardino</p></div>
<div class="area" style="left:613px;top:2440px"><div class="ph" role="img" aria-label="Palm Desert town from above" style="background:linear-gradient(180deg,#9fb7c9 0%,#b49e83 50%,#6e6a55 100%)"></div><p class="area-name">Palm Desert</p></div>

<!-- Testimonials -->
<section class="reviews"></section>
<h2 class="section-title display" style="top:2935px">Our Customer <span class="accent">Love Us</span></h2>
<div class="rule" style="top:2990px"></div>

<svg class="arrow" style="left:70px" width="20" height="20" viewBox="0 0 20 20"><path d="M13 3 6 10l7 7" stroke="#111" stroke-width="3" fill="none"/></svg>
<svg class="arrow" style="left:1110px" width="20" height="20" viewBox="0 0 20 20"><path d="m7 3 7 7-7 7" stroke="#111" stroke-width="3" fill="none"/></svg>

<div class="review" style="left:140px">
  <div class="stars"><svg width="90" height="14" viewBox="0 0 90 14"><g fill="#EE7325"><path id="s" d="M7 0l2 4.6 5 .4-3.8 3.3 1.2 5L7 10.7 2.6 13.3l1.2-5L0 5l5-.4z"/><use href="#s" x="18"/><use href="#s" x="36"/><use href="#s" x="54"/><use href="#s" x="72"/></g></svg></div>
  <h4>Sed ut perspiciatis</h4>
  <p>Lorem ipsum dolor sit amet, consectetur adipiscing elit, sed do eiusmod tempor incididunt ut labore et dolore magna aliqua. Quis ipsum suspendisse ultrices gravida. Risus commodo viverra maecenas accumsan lacus vel facilisis. Lorem ipsum dolor sit amet, consectetur adipiscing elit, sed do eiusmod tempor incididunt ut labore et dolore magna aliqua.</p>
</div>
<div class="review" style="left:457px">
  <div class="stars"><svg width="90" height="14" viewBox="0 0 90 14"><g fill="#EE7325"><use href="#s"/><use href="#s" x="18"/><use href="#s" x="36"/><use href="#s" x="54"/><use href="#s" x="72"/></g></svg></div>
  <h4 class="accent">Sed ut perspiciatis</h4>
  <p>Lorem ipsum dolor sit amet, consectetur adipiscing elit, sed do eiusmod tempor incididunt ut labore et dolore magna aliqua. Quis ipsum suspendisse ultrices gravida. Risus commodo viverra maecenas accumsan lacus vel facilisis. Lorem ipsum dolor sit amet, consectetur adipiscing elit, sed do eiusmod tempor incididunt ut labore et dolore magna aliqua.</p>
</div>
<div class="review" style="left:774px">
  <div class="stars"><svg width="90" height="14" viewBox="0 0 90 14"><g fill="#EE7325"><use href="#s"/><use href="#s" x="18"/><use href="#s" x="36"/><use href="#s" x="54"/><use href="#s" x="72"/></g></svg></div>
  <h4>Sed ut perspiciatis</h4>
  <p>Lorem ipsum dolor sit amet, consectetur adipiscing elit, sed do eiusmod tempor incididunt ut labore et dolore magna aliqua. Quis ipsum suspendisse ultrices gravida. Risus commodo viverra maecenas accumsan lacus vel facilisis. Lorem ipsum dolor sit amet, consectetur adipiscing elit, sed do eiusmod tempor incididunt ut labore et dolore magna aliqua.</p>
</div>

<!-- Reserve -->
<section class="reserve" role="img" aria-label="Industrial building and parking lot under a cloudy sky"></section>
<div class="reserve-card"></div>
<h2 class="reserve-title display">Reserve Your Event<br><span class="accent">Today!</span></h2>
<div class="form">
  <div class="row"><div class="field">First Name</div><div class="field">Last Name</div></div>
  <div class="row"><div class="field">Email Address</div><div class="field">Phone Number</div></div>
  <div class="row"><div class="field">Address</div></div>
  <div class="row"><div class="field">City</div><div class="field">Zip Code</div></div>
  <div class="row"><div class="field">Event Start Date</div><div class="field">Event Duration</div><div class="field">Number of Guests</div></div>
  <div class="row"><div class="field tall">Message</div></div>
</div>
<span class="btn btn-orange submit">Submit Now</span>

<!-- Footer -->
<div class="footer-brand"><span class="brand-box"></span>Wavelet Hire</div>
<nav class="footer-nav"><span>Home</span><span>Rent</span><span>Sell</span><span>Service Areas</span><span>Pricing</span><span>Gallery</span><span>Event</span><span>Contact</span></nav>
<div class="footer-rule"></div>
<div class="contacts">
  <div class="contact">
    <svg width="34" height="34" viewBox="0 0 34 34"><circle cx="17" cy="17" r="17" fill="#EE7325"/><path d="M17 9a5.5 5.5 0 0 0-5.5 5.5C11.5 18.5 17 25 17 25s5.5-6.5 5.5-10.5A5.5 5.5 0 0 0 17 9zm0 7.5a2 2 0 1 1 0-4 2 2 0 0 1 0 4z" fill="#fff"/></svg>
    <span>123 Street name, City name,<br>Santa Ana California 123 456</span>
  </div>
  <div class="contact">
    <svg width="34" height="34" viewBox="0 0 34 34"><circle cx="17" cy="17" r="17" fill="#EE7325"/><path d="M12 10h3l1.5 4-2 1.3a9 9 0 0 0 4.2 4.2L20 17.5l4 1.5v3a2 2 0 0 1-2 2A12 12 0 0 1 10 12a2 2 0 0 1 2-2z" fill="#fff"/></svg>
    <span>(123)456-7890</span>
  </div>
  <div class="contact">
    <svg width="34" height="34" viewBox="0 0 34 34"><circle cx="17" cy="17" r="17" fill="#EE7325"/><rect x="9" y="11" width="16" height="12" rx="1.5" fill="#fff"/><path d="m9.5 12 7.5 6 7.5-6" stroke="#EE7325" stroke-width="1.5" fill="none"/></svg>
    <span>hello@wavelethire.com</span>
  </div>
</div>
<p class="copy">© 2024 Wavelet Hire - All Rights Reserved</p>
<div class="socials"><span class="social"></span><span class="social"></span><span class="social"></span><span class="social"></span></div>

</body>
</html>
```